Financial Services Firm - Prospective Partnership Marketing Brochure

What business are we in? Larkstone Financial Management (LFM) was founded to provide payroll, bookkeeping, bill paying, debt management, and financial aggregation services for individuals and small businesses seeking relief from the details associated with their financial matters — clerical tasks that our customers either cannot or prefer not to perform. At its core, our service is often referred to as Daily Money Management. As leaders in the Daily Money Management field, we leverage financial controls, technology and concierge-like personal attention in order to maximize the convenience our service provides for our business and individual clients. LFM complements the work of other professionals by completing day-to-day tasks rather than long-term plans. The services meet a continuum of needs, from organizing and keeping track of financial information, book keeping, and investment tracking, to assisting with bill paying and maintaining bank accounts and insurance.
We need a design for a marketing brochure with the following specs:
Four-panel brochure with a double gatefold.
➢ Unfolded: 15 x 9
➢ Finished size: 3 3/4 x 9
Purpose - To convey key information about LFM.
“Look and feel” - Needs to be professional, “corporate” and information showcased must be “top-line”.
Primary Targets - High net-worth individuals, small business owners, on-the-go professionals and individuals
Purpose - To convey key information about LFM to potential business partners.
“Look and feel” - Needs to be professional, “corporate” and information showcased must be “top-line”. These are busy professional people, so less is more.
Primary Targets – Financial Planners
Current company logo, letterhead, business card design, and brochure content details attached for reference.

```html
<!DOCTYPE html>
<html lang="en">
<head>
<meta charset="utf-8">
<title>Larkstone Financial Management – Partner Brochure</title>
<link rel="stylesheet" href="https://fonts.googleapis.com/css2?family=Source+Sans+3:wght@300;400;600;700&display=swap">
<style>
  :root {
    --stage: #1f1f1f;
    --panel-top: #5b5b5b;
    --panel-bottom: #464646;
    --divider: #8a8a8a;
    --white: #ffffff;
    --soft-white: #e6e6e6;
    --accent-blue: #2a9fd8;
    --brand-gray: #474747;
    --tag-strong: #c4823f;
    --tag-soft: #d9a66f;
    --footer-black: #0b0b0b;
  }
  * { box-sizing: border-box; margin: 0; padding: 0; }
  html, body { width: 1200px; height: 793px; overflow: hidden; }
  body {
    background: var(--stage);
    font-family: "Source Sans 3", "Myriad Pro", Arial, sans-serif;
    position: relative;
    color: var(--white);
  }

  /* ---------- Back panel ---------- */
  .panel { position: absolute; top: 44px; height: 706px; overflow: hidden; }
  .panel--partner { left: 232px; width: 310px; background: var(--panel-bottom); }
  .partner-top {
    position: absolute; inset: 0 0 auto 0; height: 288px; background: var(--panel-top);
  }
  .partner-divider {
    position: absolute; left: 0; right: 0; top: 288px; height: 5px; background: var(--divider);
  }
  .brand {
    position: absolute; display: flex; align-items: center; gap: 8px;
  }
  .brand__mark { width: 14px; height: 14px; background: var(--accent-blue); flex: none; }
  .brand__name { font-weight: 600; text-transform: uppercase; line-height: 1.05; }
  .panel--partner .brand { top: 46px; left: 0; right: 0; justify-content: center; }
  .panel--partner .brand__name { color: var(--white); font-size: 17px; letter-spacing: 2px; text-align: left; }
  .contact {
    position: absolute; top: 150px; left: 40px; right: 40px;
    text-align: center; font-size: 7.5px; line-height: 1.45; color: var(--soft-white);
  }
  .contact b { font-weight: 700; }
  .partner-photo {
    position: absolute; left: 0; top: 293px; width: 150px; bottom: 0;
    background: linear-gradient(180deg, #6b5446 0%, #8d7566 30%, #9aa0a6 62%, #7c8288 100%);
  }
  .headline {
    position: absolute; top: 312px; left: 112px; right: 10px;
    font-weight: 300; text-transform: uppercase; line-height: 1.02; color: var(--white);
  }
  .headline span { display: block; }
  .headline .l1 { font-size: 19px; }
  .headline .l2 { font-size: 25px; }
  .headline .l3 { font-size: 34px; }
  .partner-copy {
    position: absolute; top: 424px; left: 118px; right: 14px;
    font-size: 10.5px; line-height: 1.3; text-align: center; color: var(--white);
  }
  .partner-copy p + p { margin-top: 12px; }
  .partner-copy strong { font-weight: 700; }
  .partner-copy small { font-size: 6.5px; }
  .hours {
    position: absolute; bottom: 28px; right: 16px;
    font-size: 7.5px; line-height: 1.35; text-align: right; color: var(--white);
  }
  .hours strong { font-weight: 700; }

  /* ---------- Front panel ---------- */
  .panel--cover {
    left: 652px; width: 290px;
  }
  .cover-photo {
    position: absolute; inset: 0 0 34px 0;
    background:
      linear-gradient(180deg, #b8b69a 0%, #e6dfbf 22%, #efe4c0 38%, #b5a47a 52%, #8f7f56 70%, #6d6a45 86%, #4e5234 100%);
  }
  .panel--cover .brand {
    top: 52px; left: 0; right: 0; justify-content: center;
  }
  .panel--cover .brand__mark { width: 18px; height: 18px; }
  .panel--cover .brand__name { color: var(--brand-gray); font-size: 22px; letter-spacing: 3px; }
  .tagline {
    position: absolute; top: 236px; left: 24px; width: 170px;
    font-size: 11.5px; line-height: 1.22; color: var(--tag-soft);
  }
  .tagline strong { color: var(--tag-strong); font-weight: 700; }
  .cover-footer {
    position: absolute; left: 0; right: 0; bottom: 0; height: 34px;
    background: var(--footer-black); color: var(--white);
    font-size: 9px; display: flex; align-items: center; justify-content: center;
  }
</style>
</head>
<body>

  <section class="panel panel--partner">
    <div class="partner-top"></div>
    <div class="partner-divider"></div>

    <div class="brand">
      <span class="brand__mark"></span>
      <span class="brand__name">Larkstone<br>Financial Management</span>
    </div>

    <div class="contact">
      <p><b>P:</b> (480) 555-0172</p>
      <p><b>M:</b> info@larkstonefm.com</p>
      <p><b>A:</b> Larkstone Financial Management, 2210 W.<br>Quarry Ridge Dr, Mesa, AZ 85201</p>
    </div>

    <div class="partner-photo" role="img" aria-label="Photo of a smiling businesswoman in a gray suit with arms crossed"></div>

    <h1 class="headline">
      <span class="l1">Become an</span>
      <span class="l2">LFM Partner</span>
      <span class="l3">Today!</span>
    </h1>

    <div class="partner-copy">
      <p><strong>For a free consultation</strong> on becoming an LFM Partner, contact us today.</p>
      <p>An LFM representative will normally respond to all inquiries within 2 to 24 hours <small>(excluding weekends and holidays)</small>.</p>
    </div>

    <div class="hours">
      <strong>LFM office hours:</strong><br>
      Monday - Friday<br>
      from 9:00 AM to 5:00 PM MST.
    </div>
  </section>

  <section class="panel panel--cover">
    <div class="cover-photo" role="img" aria-label="Photo of a businessman in a dark suit shading his eyes, looking into the distance on a grassy hillside under a hazy sky"></div>

    <div class="brand">
      <span class="brand__mark"></span>
      <span class="brand__name">Larkstone<br>Financial Management</span>
    </div>

    <p class="tagline"><strong>Expanding your Financial</strong><br>Planning business<br>begins with a<br>. . .Larkstone.</p>

    <footer class="cover-footer">www.larkstonefm.com</footer>
  </section>

</body>
</html>
```